Cover für Hauptkatalog
Zielgruppe
TESSARIN GmbH ist ein führender Großhändler in der Hobby- und Bastelbranche. mit unseren weit über 8.000 Produkten beliefern wir Einzelhändler in ganz Europa. Durch unsere Größe sind wir in der Lage sehr schnell auf individuelle Kundenwünsche zu reagieren.
Aufgabenstellung
Wir werden Mitte Dezember einen neuen Kreativ-Katalog mit über 450 Seiten unseren Kunden zur Verfügung stellen. In diesem Zusammenhang soll der Umschlag (Vorder- und Rückseite) in einem neuen, frischen Design erscheinen. Das aktuelle Layout kann unter www.tessarin-hobby.example eingesehen werden. Auf der Rückseite soll unsere Adresse stehen.

```html
<!DOCTYPE html>
<html lang="de">
<head>
<meta charset="utf-8">
<title>TESSARIN – Katalogumschlag</title>
<link rel="stylesheet" href="https://fonts.googleapis.com/css2?family=Lato:wght@300;400;700;900&display=swap">
<style>
  :root {
    --brand-blue: #233e8b;
    --brand-red: #d43d2a;
    --paper: #ffffff;
    --edge: #c8c8c8;
    --tile: 171px;
  }
  * { margin: 0; padding: 0; box-sizing: border-box; }
  html, body { width: 1200px; height: 847px; overflow: hidden; background: var(--paper); }
  body { font-family: "Lato", sans-serif; color: var(--brand-blue); }
  .cover {
    position: relative; width: 1200px; height: 847px;
    border: 1px solid var(--edge); background: var(--paper);
  }
  .tile { position: absolute; width: var(--tile); height: var(--tile); }
  .tile--red { background: var(--brand-red); }
  .tile--blue { background: var(--brand-blue); }
  .tile--blank { background: var(--paper); border: 1px solid #444; }
  .tile--table { background: linear-gradient(160deg, #dff0f5, #a9d6e2 55%, #f4f1ea); }
  .tile--owl { background: linear-gradient(150deg, #f4f4f2, #e6e7ea 50%, #4fa9c7 75%, #e7e3e4); }
  .tile--blooms { background: radial-gradient(circle at 55% 40%, #d7c9e0, #8fbd5c 45%, #4f8a38); }
  .tile--beads { background: radial-gradient(circle at 50% 50%, #f3ea4a, #bddc74 45%, #dcebc4); }
  .tile--bowls { background: linear-gradient(170deg, #4d7a3a, #9cc1d4 40%, #8fb3c2 75%, #6b8b5e); }
  .tile--pinwheels { background: linear-gradient(160deg, #a8a3c0, #e88ac0 40%, #7fa6d9 65%, #9aa07a); }

  .brand { position: absolute; display: flex; align-items: center; gap: 8px; font-weight: 900; color: var(--brand-blue); letter-spacing: -0.5px; }
  .brand__square { background: var(--brand-red); }
  .brand--top { left: 29px; top: 432px; font-size: 44px; }
  .brand--top .brand__square { width: 30px; height: 30px; }
  .brand--bottom { right: 32px; top: 722px; font-size: 62px; }
  .brand--bottom .brand__square { width: 42px; height: 42px; }

  .claim { position: absolute; right: 32px; top: 416px; text-align: right; font-weight: 300; line-height: 1; }
  .claim__de { font-size: 60px; }
  .claim__fr { font-size: 41px; margin-top: 13px; }
  .claim__en { font-size: 43px; margin-top: 12px; }

  .info { position: absolute; left: 29px; top: 535px; font-size: 15.5px; font-weight: 300; line-height: 19.5px; }

  .address { position: absolute; top: 636px; font-size: 17.5px; font-weight: 300; line-height: 20.2px; }
  .address__name { font-weight: 400; }
  .address--ch { left: 28px; }
  .address--de { left: 282px; }

  .web { position: absolute; left: 28px; top: 784px; font-size: 34px; font-weight: 300; }
</style>
</head>
<body>
<main class="cover">
  <div class="tile tile--table" style="left:32px;top:31px" role="img" aria-label="Festlich gedeckter Tisch mit Gläsern, Kerze und Muffins"></div>
  <div class="tile tile--red" style="left:218px;top:31px"></div>
  <div class="tile tile--owl" style="left:403px;top:31px" role="img" aria-label="Gebastelte türkise Eule neben Windlichtern"></div>
  <div class="tile tile--red" style="left:627px;top:31px"></div>
  <div class="tile tile--blooms" style="left:809px;top:31px" role="img" aria-label="Bunte Bastelblumen im Garten"></div>
  <div class="tile tile--blue" style="left:989px;top:31px"></div>

  <div class="tile tile--blank" style="left:33px;top:222px"></div>
  <div class="tile tile--beads" style="left:218px;top:222px" role="img" aria-label="Gelbe und grüne Perlenketten mit Satinband"></div>
  <div class="tile tile--blue" style="left:404px;top:222px"></div>
  <div class="tile tile--bowls" style="left:627px;top:222px" role="img" aria-label="Blau gemusterte Schalen und grüne Äpfel auf Gartentisch"></div>
  <div class="tile tile--blank" style="left:808px;top:222px"></div>
  <div class="tile tile--pinwheels" style="left:989px;top:222px" role="img" aria-label="Bunte Windräder vor Lavendel"></div>

  <div class="brand brand--top"><span>TESSARIN</span><span class="brand__square"></span></div>

  <h1 class="claim">
    <div class="claim__de">Freude an Kreativität</div>
    <div class="claim__fr">Plaisir de créer</div>
    <div class="claim__en">Creative pleasure</div>
  </h1>

  <p class="info">
    Weitere Informationen und Bezugsquellennachweis<br>
    Pour toute information complementaire et liste de revendeurs<br>
    Further information and documentation can be obtained from
  </p>

  <address class="address address--ch">
    <div class="address__name">TESSARIN AG</div>
    Lindenweg 8<br>
    CH-4999 Talwiesen<br>
    Phone: +41 00 555 01 20<br>
    Fax: +41 00 555 01 21<br>
    info@tessarin.example
  </address>

  <address class="address address--de">
    <div class="address__name">TESSARIN GmbH</div>
    Mühlenstrasse 4<br>
    D-79999 Bergfelden<br>
    Phone: +49 0000 5550 0<br>
    Fax: +49 0000 5551<br>
    info@tessarin-hobby.example
  </address>

  <div class="web">www.tessarin-hobby.example</div>

  <div class="brand brand--bottom"><span>TESSARIN</span><span class="brand__square"></span></div>
</main>
</body>
</html>
```